Mavurena website
www.mavurena.org
Mavurena is a non profit organization that aims to build a Tolvanne hospital in Burkina Faso, West Africa, that will offer free medical services for physical restoration and rehabilitation for FGM victims.

```html
<!DOCTYPE html>
<html lang="en">
<head>
<meta charset="utf-8">
<title>Mavurena – Helping victims of FGM</title>
<link rel="stylesheet" href="https://fonts.googleapis.com/css2?family=Arimo:wght@400;700&display=swap">
<style>
  :root {
    --bg-top: #c6d0ea;
    --bg-bottom: #ffffff;
    --nav-active: #e8640e;
    --nav-yellow: #f3d41a;
    --nav-border: #fbe98a;
    --sidebar: #f6e31c;
    --white: #ffffff;
    --ink: #333333;
    --muted: #555555;
    --brand: #3a3a3a;
    --tagline: #7a5a2a;
    --social-box: rgba(225, 228, 236, 0.92);
    --link: #3b5a9a;
    --hero-dark: #3a2418;
    --hero-warm: #8a4a2a;
    --hero-red: #c42a1c;
  }
  html, body {
    margin: 0;
    width: 1200px;
    height: 806px;
    overflow: hidden;
  }
  body {
    background: linear-gradient(180deg, var(--bg-top) 0%, #e4e9f6 55%, var(--bg-bottom) 100%);
    font-family: "Arimo", Arial, sans-serif;
    color: var(--ink);
  }
  .page {
    position: relative;
    width: 1200px;
    height: 806px;
  }
  .site {
    position: absolute;
    left: 175px;
    top: 0;
    width: 845px;
    height: 806px;
    background: var(--white);
  }
  .hero {
    position: absolute;
    left: 0;
    top: 0;
    width: 845px;
    height: 504px;
    background:
      radial-gradient(ellipse at 40% 45%, var(--hero-warm) 0%, transparent 45%),
      radial-gradient(ellipse at 72% 70%, var(--hero-red) 0%, transparent 35%),
      linear-gradient(135deg, #4d6a3a 0%, var(--hero-dark) 45%, #5a3020 100%);
  }
  .masthead {
    position: absolute;
    left: 0;
    top: 0;
    width: 845px;
    height: 108px;
    background: rgba(255, 255, 255, 0.82);
  }
  .brand {
    position: absolute;
    left: 22px;
    top: 8px;
    display: flex;
    align-items: center;
    gap: 16px;
  }
  .brand-mark {
    width: 62px;
    height: 62px;
    border-radius: 50%;
    background: var(--nav-yellow);
  }
  .brand-name {
    font-size: 52px;
    font-weight: 700;
    letter-spacing: 2px;
    color: var(--brand);
    line-height: 1;
    text-transform: uppercase;
  }
  .tagline {
    position: absolute;
    left: 100px;
    top: 74px;
    font-family: "Arimo", Arial, sans-serif;
    font-size: 19px;
    font-weight: 400;
    color: var(--tagline);
    letter-spacing: 0.5px;
  }
  .social {
    position: absolute;
    right: 12px;
    top: 10px;
    width: 96px;
    height: 92px;
    background: var(--social-box);
    padding: 8px 0 0 10px;
    box-sizing: border-box;
    list-style: none;
    margin: 0;
  }
  .social li {
    display: flex;
    align-items: center;
    gap: 6px;
    height: 25px;
    font-size: 12px;
    color: var(--link);
  }
  .social .dot {
    width: 14px;
    height: 14px;
    background: var(--link);
  }
  .main-nav {
    position: absolute;
    left: 17px;
    top: 186px;
    width: 150px;
    margin: 0;
    padding: 0;
    list-style: none;
  }
  .main-nav li {
    height: 48px;
    margin-bottom: 5px;
    background: var(--nav-yellow);
    border: 1px solid var(--nav-border);
    box-sizing: border-box;
    color: var(--white);
    font-size: 19px;
    display: flex;
    align-items: center;
    justify-content: center;
  }
  .main-nav li.is-active {
    background: var(--nav-active);
  }
  .sidebar {
    position: absolute;
    left: 0;
    top: 504px;
    width: 173px;
    height: 302px;
    background: var(--sidebar);
    text-align: center;
  }
  .sidebar h2 {
    margin: 24px 0 2px;
    font-size: 20px;
    font-weight: 400;
    color: var(--ink);
  }
  .sidebar h3 {
    margin: 0 0 4px;
    font-size: 13px;
    font-weight: 700;
    color: var(--ink);
  }
  .sidebar p {
    margin: 0 18px;
    font-size: 10px;
    line-height: 12px;
    color: var(--muted);
  }
  .news-photo {
    display: block;
    width: 144px;
    height: 84px;
    margin: 14px auto 0;
    background: linear-gradient(180deg, #9fb7d6 0%, #c9a27a 60%, #8aa06a 100%);
  }
  .copyright {
    position: absolute;
    left: 0;
    bottom: 8px;
    width: 100%;
    font-size: 10px;
    color: var(--muted);
  }
  .content h1 {
    position: absolute;
    left: 225px;
    top: 532px;
    margin: 0;
    font-size: 27px;
    font-weight: 400;
    color: var(--ink);
  }
  .feature-photo {
    position: absolute;
    left: 225px;
    top: 571px;
    width: 272px;
    height: 161px;
    background: linear-gradient(180deg, #8e9aa4 0%, #6d7a70 45%, #b9b6ad 100%);
  }
  .content p {
    position: absolute;
    left: 538px;
    top: 567px;
    width: 296px;
    margin: 0;
    font-size: 10.5px;
    line-height: 14.5px;
    color: var(--muted);
  }
  .footer-nav {
    position: absolute;
    right: 16px;
    top: 784px;
    margin: 0;
    padding: 0;
    list-style: none;
    display: flex;
    gap: 8px;
    font-size: 11px;
    color: var(--muted);
  }
  .footer-nav li + li::before {
    content: "·";
    margin-right: 8px;
  }
</style>
</head>
<body>
<div class="page">
  <div class="site">
    <div class="hero" role="img" aria-label="Photograph of two smiling women posing together"></div>

    <header class="masthead">
      <div class="brand">
        <span class="brand-mark"></span>
        <span class="brand-name">Mavurena</span>
      </div>
      <div class="tagline">Restoring a Sense of Dignity &amp; Pleasure</div>
      <ul class="social">
        <li><span class="dot"></span>Chirpline</li>
        <li><span class="dot"></span>Orbitplus</li>
        <li><span class="dot"></span>Pagebook</li>
      </ul>
    </header>

    <ul class="main-nav">
      <li class="is-active">Home</li>
      <li>About Us</li>
      <li>Donate</li>
      <li>News</li>
      <li>Contact Us</li>
    </ul>

    <aside class="sidebar">
      <h2>News</h2>
      <h3>New Hospital Open</h3>
      <p>Lorem ipsum dolor sit amet, consectetur adipiscing elit. Nam diam turpis, molestie in luctus vitae, pulvinar vitae elit. Morbi commodo congue lorem eu placerat.</p>
      <span class="news-photo" role="img" aria-label="Photograph of the new Tolvanne hospital building"></span>
      <div class="copyright">Copyright Mavurena 2012</div>
    </aside>

    <main class="content">
      <h1>Helping victims of FGM</h1>
      <div class="feature-photo" role="img" aria-label="Photograph of a woman sitting on rocks by a waterfall"></div>
      <p>Lorem ipsum dolor sit amet, consectetur adipiscing elit. Nam diam turpis, molestie in luctus vitae, pulvinar vitae elit. Morbi commodo congue lorem eu placerat. Nulla luctus feugiat tempus. Nunc in turpis in eros fringilla mattis a vitae neque. Integer non nibh enim, eget blandit lacus. Sed non libero varius ante eleifend non, pretium non mauris. Cras tincidunt elementum enim vel dapibus. Quisque varius turpis sed turpis egestas in lacinia turpis aliquet. In ac tortor sit amet augue facilisis tincidunt vitae quis nisi. Sed lobortis malesuada posuere. Integer id odio eros. Nunc id elit tortor, id cursus mauris. Curabitur in faucibus dolor.</p>
    </main>

    <ul class="footer-nav">
      <li>Home</li>
      <li>About Us</li>
      <li>Donate</li>
      <li>News</li>
      <li>Contact Us</li>
      <li>Privacy Policy</li>
      <li>Site Map</li>
    </ul>
  </div>
</div>
</body>
</html>
```